Business Card desgin, company called Stand Fast.

I am looking for the logo colors (3) to be used on the card in whatever design you think might work. the certifications are on the back (4) on the front will be my name, Dana Whitlock, owner/instructor, phone 208.555.0193, website www.sfx-drills.example, email dw@sfx-drills.example. im flexible on fonts.

Target Market(s)

firearms owners

Industry/Entity Type

firearms training

Contact Information for Business Card

certification icons on back

```html
<!DOCTYPE html>
<html lang="en">
<head>
<meta charset="utf-8">
<title>Stand Fast – Business Card</title>
<link href="https://fonts.googleapis.com/css2?family=Lexend:wght@400;700&family=Montserrat:wght@700&display=swap" rel="stylesheet">
<style>
  :root {
    --backdrop: #cccccc;
    --navy: #0f2944;
    --red: #b91f2e;
    --white: #ffffff;
    --silver-light: #f4f4f4;
    --silver-dark: #9a9a9a;
    --badge-fill: #dde1e6;
  }
  * { margin: 0; padding: 0; box-sizing: border-box; }
  html, body {
    width: 1200px; height: 1112px; overflow: hidden;
    background: var(--backdrop);
  }
  .canvas { position: relative; width: 1200px; height: 1112px; }
  .card {
    position: absolute; width: 753px; height: 443px;
    background: var(--navy); overflow: hidden;
  }
  .card--front { left: 75px; top: 75px; }
  .card--back { left: 372px; top: 593px; }
  .corner { position: absolute; left: 0; top: 0; }

  /* front */
  .brand {
    position: absolute; left: 88px; top: 76px; width: 132px;
    display: flex; flex-direction: column; align-items: center;
  }
  .brand__name {
    font-family: "Montserrat", sans-serif; font-weight: 700;
    font-size: 18px; color: var(--red); letter-spacing: 0.2px;
    white-space: nowrap;
  }
  .brand__circle { margin-top: 8px; }
  .brand__url {
    margin-top: 6px; font-family: "Montserrat", sans-serif; font-weight: 700;
    font-size: 7.5px; color: var(--white); white-space: nowrap;
  }
  .next-arrow { position: absolute; left: 649px; top: 339px; }

  /* back */
  .back-mark {
    position: absolute; left: 86px; top: 166px; width: 116px; height: 116px;
    border-radius: 50%; border: 4px solid var(--white);
    display: flex; align-items: center; justify-content: center;
  }
  .back-mark__name {
    font-family: "Lexend", sans-serif; font-weight: 700; font-size: 17px;
    color: var(--red); text-align: center; line-height: 1.1;
  }
  .divider {
    position: absolute; left: 255px; top: 118px; width: 3px; height: 208px;
    background: var(--red);
  }
  .person { position: absolute; left: 297px; top: 114px; }
  .person__name {
    font-family: "Lexend", sans-serif; font-weight: 700; font-size: 41px;
    color: var(--white); letter-spacing: -0.3px; line-height: 1; white-space: nowrap;
  }
  .person__role {
    margin-top: 10px; font-family: "Lexend", sans-serif; font-weight: 400;
    font-size: 16px; color: var(--red); letter-spacing: 0.3px;
  }
  .contacts { position: absolute; left: 297px; top: 218px; list-style: none; }
  .contacts li {
    display: flex; align-items: center; height: 28px; margin-bottom: 10px;
    font-family: "Lexend", sans-serif; font-size: 18.5px; color: var(--white);
    white-space: nowrap;
  }
  .contacts svg { width: 22px; height: 22px; margin-right: 14px; flex: none; }
  .cert-strip {
    position: absolute; right: 0; top: 0; width: 101px; height: 443px;
    background: var(--white); border-left: 7px solid var(--red);
  }
  .badge {
    position: absolute; left: 19px; width: 56px; height: 56px;
    border-radius: 8px; background: var(--badge-fill);
  }
</style>
</head>
<body>
<div class="canvas">

  <section class="card card--front">
    <svg class="corner" width="160" height="160" viewBox="0 0 160 160">
      <defs>
        <linearGradient id="silver" x1="0" y1="0" x2="1" y2="1">
          <stop offset="0" stop-color="var(--silver-light)"/>
          <stop offset="0.5" stop-color="var(--silver-dark)"/>
          <stop offset="1" stop-color="var(--silver-light)"/>
        </linearGradient>
      </defs>
      <polygon points="0,0 150,0 0,150" fill="url(#silver)"/>
      <polygon points="0,0 128,0 0,128" fill="var(--red)"/>
    </svg>
    <div class="brand">
      <span class="brand__name">STAND FAST</span>
      <svg class="brand__circle" width="118" height="118" viewBox="0 0 118 118">
        <circle cx="59" cy="59" r="55" fill="none" stroke="var(--white)" stroke-width="4"/>
      </svg>
      <span class="brand__url">WWW.SFX-DRILLS.EXAMPLE</span>
    </div>
    <svg class="next-arrow" width="58" height="58" viewBox="0 0 58 58">
      <circle cx="29" cy="29" r="27.5" fill="none" stroke="var(--white)" stroke-width="2"/>
      <path d="M12 29 H45 M34 18 L45 29 L34 40" fill="none" stroke="var(--white)" stroke-width="2" stroke-linecap="round" stroke-linejoin="round"/>
    </svg>
  </section>

  <section class="card card--back">
    <svg class="corner" width="160" height="160" viewBox="0 0 160 160">
      <defs>
        <linearGradient id="silver2" x1="0" y1="0" x2="1" y2="1">
          <stop offset="0" stop-color="var(--silver-light)"/>
          <stop offset="0.5" stop-color="var(--silver-dark)"/>
          <stop offset="1" stop-color="var(--silver-light)"/>
        </linearGradient>
      </defs>
      <polygon points="0,0 150,0 0,150" fill="url(#silver2)"/>
      <polygon points="0,0 128,0 0,128" fill="var(--red)"/>
    </svg>

    <div class="back-mark"><span class="back-mark__name">Stand<br>Fast</span></div>
    <div class="divider"></div>

    <div class="person">
      <h1 class="person__name">Dana Whitlock</h1>
      <p class="person__role">owner/instructor</p>
    </div>

    <ul class="contacts">
      <li>
        <svg viewBox="0 0 24 24" fill="none" stroke="var(--white)" stroke-width="1.4" stroke-linejoin="round">
          <path d="M5 3 L9 3 L10.5 7.5 L8 9.5 C9.5 12.5 11.5 14.5 14.5 16 L16.5 13.5 L21 15 L21 19 C21 20 20 21 19 21 C10.5 20.5 3.5 13.5 3 5 C3 4 4 3 5 3 Z"/>
        </svg>
        208.555.0193
      </li>
      <li>
        <svg viewBox="0 0 24 24" fill="none" stroke="var(--white)" stroke-width="1.2">
          <circle cx="12" cy="12" r="9.5"/>
          <ellipse cx="12" cy="12" rx="4.5" ry="9.5"/>
          <path d="M2.5 12 H21.5 M4 7 H20 M4 17 H20 M12 2.5 V21.5"/>
        </svg>
        www.sfx-drills.example
      </li>
      <li>
        <svg viewBox="0 0 24 24" fill="none" stroke="var(--white)" stroke-width="1.2">
          <circle cx="12" cy="12" r="10"/>
          <rect x="6.5" y="8" width="11" height="8"/>
          <path d="M6.5 8 L12 12.5 L17.5 8 M6.5 16 L10.5 11.5 M17.5 16 L13.5 11.5"/>
        </svg>
        dw@sfx-drills.example
      </li>
    </ul>

    <aside class="cert-strip" aria-label="Certifications">
      <div class="badge" style="top:43px" role="img" aria-label="Certification badge placeholder"></div>
      <div class="badge" style="top:137px" role="img" aria-label="Certification badge placeholder"></div>
      <div class="badge" style="top:238px" role="img" aria-label="Certification badge placeholder"></div>
      <div class="badge" style="top:339px" role="img" aria-label="Certification badge placeholder"></div>
    </aside>
  </section>

</div>
</body>
</html>
```